Home based handmade craft items business card

I need a business card design for my new venture 'Lindqvist Homemade'. As the 'homemade' suggests I design and create handmade cards, invitations and I have recently branched out into mixed media canvases and tote (patchwork) bags to sell at markets. I also go into peoples homes and do workshops and make-n-takes to sell Plomberly products. Plomberly do have their own website if you are interested to look it is: www.plomberly-crafts.example
I find that women and children are my main purchasers/workshop attendees and I would like my business card to reflect this.
I like Dorrow Lane, vintage, steam punk and I LOVE RAY BENNICK designs colours, I like, browns, greens and pinks.
In my minds eye I had seen the card having Lindqvist Homemade surrounded by a soft vine with a butterfly sitting on the vine in one corner....with a soft vintage lace effect in the background.
Target Market(s)
People who love to create or those that don't create but would love to buy creative homemade craft items
Industry/Entity Type
Business
Contact Information for Business Card
Lindqvist Handmade
Marlene Lindqvist
Tarrowby
0437 902584
Independent Plomberly Consultant #382947 - sales, workshops and Make-n-Takes
Handmade cards & invitations
Mixed Media Canvases
and lots of other Handmade goodies..
Logo Text
Lindqvist Homemade

```html
<!DOCTYPE html>
<html lang="en">
<head>
<meta charset="utf-8">
<title>Lindqvist Homemade – Business Card</title>
<link rel="stylesheet" href="https://fonts.googleapis.com/css2?family=Pinyon+Script&family=Parisienne&family=Quicksand:wght@400;500&family=Josefin+Sans:wght@400&display=swap">
<style>
  :root {
    --page: #e9e5e0;
    --chocolate: #2e1414;
    --chocolate-deep: #221010;
    --gold: #e3c98a;
    --gold-light: #fbf1c8;
    --gold-mid: #eedca0;
    --gold-dark: #b8934c;
    --ruby: #9c1414;
    --ruby-light: #c52a24;
    --ruby-dark: #5e0a0a;
    --ink: #3a1d14;
  }
  * { box-sizing: border-box; margin: 0; padding: 0; }
  html, body { width: 1200px; height: 1000px; overflow: hidden; }
  body {
    background: var(--page);
    display: flex;
    flex-direction: column;
    align-items: center;
    justify-content: space-evenly;
  }
  .card {
    width: 735px;
    height: 420px;
    position: relative;
    overflow: hidden;
    box-shadow: 0 6px 18px rgba(40, 20, 10, 0.25);
  }

  /* Back side */
  .card-back {
    background: var(--chocolate);
    color: var(--gold);
    text-align: center;
  }
  .identity {
    position: absolute;
    top: 100px;
    left: 0;
    right: 0;
    display: flex;
    justify-content: center;
  }
  .identity-block {
    display: inline-flex;
    flex-direction: column;
    align-items: flex-end;
  }
  .identity-name {
    font-family: "Pinyon Script", cursive;
    font-size: 38px;
    line-height: 1.1;
    color: var(--gold);
    white-space: nowrap;
  }
  .identity-title {
    font-family: "Josefin Sans", sans-serif;
    font-size: 10px;
    letter-spacing: 1.5px;
    text-transform: uppercase;
    line-height: 1.2;
    white-space: nowrap;
  }
  .identity-number {
    font-family: "Pinyon Script", cursive;
    font-size: 22px;
    line-height: 1.1;
    white-space: nowrap;
  }
  .phone {
    position: absolute;
    top: 206px;
    left: 0;
    right: 0;
    font-family: "Quicksand", sans-serif;
    font-size: 18px;
    letter-spacing: 1px;
    color: var(--gold-dark);
  }
  .services {
    position: absolute;
    top: 270px;
    left: 0;
    right: 0;
    font-family: "Parisienne", cursive;
    font-size: 16px;
    line-height: 1.5;
    color: var(--gold);
  }

  /* Front side */
  .card-front {
    background: linear-gradient(180deg, var(--gold-light) 0%, var(--gold-mid) 55%, var(--gold) 100%);
  }
  .lace-band {
    position: absolute;
    left: 0;
    right: 0;
    height: 62px;
    background: linear-gradient(180deg, var(--chocolate) 0%, var(--chocolate-deep) 100%);
  }
  .lace-band--top { top: 0; }
  .lace-band--bottom { bottom: 0; transform: scaleY(-1); }
  .lace-band::after {
    content: "";
    position: absolute;
    left: 0;
    right: 0;
    bottom: 0;
    height: 18px;
    background: linear-gradient(180deg, var(--chocolate-deep), #c9a868);
    opacity: 0.55;
  }
  .ruby-rule {
    position: absolute;
    left: 0;
    right: 0;
    height: 3px;
    background: var(--ruby);
  }
  .ruby-rule--top { top: 74px; }
  .ruby-rule--bottom { bottom: 74px; }
  .ornament {
    position: absolute;
    left: 50%;
    top: 50%;
    width: 480px;
    height: 210px;
    transform: translate(-50%, -50%);
    border-radius: 50%;
    background: radial-gradient(ellipse at center, rgba(58, 29, 20, 0.35) 0%, rgba(58, 29, 20, 0.18) 45%, rgba(58, 29, 20, 0) 72%);
  }
  .plaque {
    position: absolute;
    left: 50%;
    top: 50%;
    width: 330px;
    height: 112px;
    transform: translate(-50%, -50%);
    border-radius: 36px;
    border: 4px solid var(--ink);
    box-shadow: 0 0 0 2px var(--gold-dark);
    background: radial-gradient(ellipse at 40% 40%, var(--ruby-light) 0%, var(--ruby) 55%, var(--ruby-dark) 100%);
    display: flex;
    align-items: center;
    justify-content: center;
  }
  .brand-name {
    font-family: "Pinyon Script", cursive;
    font-size: 34px;
    color: var(--gold);
    white-space: nowrap;
  }
</style>
</head>
<body>

  <article class="card card-back">
    <div class="identity">
      <div class="identity-block">
        <p class="identity-name">Marlene Lindqvist Tarrowby</p>
        <span class="identity-title">Independent Plomberly Consultant</span>
        <span class="identity-number">#382947</span>
      </div>
    </div>
    <p class="phone">phone: 0437 902584</p>
    <div class="services">
      <p>Sales workshops and Make-n-Takes Handmade</p>
      <p>cards &amp; invitations Mixed Media Canvases</p>
      <p>lots of other Handmade goodies</p>
    </div>
  </article>

  <article class="card card-front">
    <div class="lace-band lace-band--top" role="img" aria-label="Vintage lace border with diamond pattern in chocolate and gold"></div>
    <div class="ruby-rule ruby-rule--top"></div>
    <div class="ornament" role="img" aria-label="Ornamental swirling vine flourishes around the name plaque"></div>
    <div class="plaque">
      <span class="brand-name">Lindqvist Homemade</span>
    </div>
    <div class="ruby-rule ruby-rule--bottom"></div>
    <div class="lace-band lace-band--bottom" role="img" aria-label="Vintage lace border with diamond pattern in chocolate and gold"></div>
  </article>

</body>
</html>
```